Speisekarten-Design für italienisches Restaurant im Golfclub mit Blick auf die Alpen
Zielgruppe
Italienisches Restaurant im Golfclub mit Blick auf die Alpen (bei gutem Wetter)
Aufgabenstellung
Karte muss weiterhin bearbeitet werden könne. Es geht um ein Design das optisch anspricht aber nicht übertrieben ist. Die Blätter kommen später in eine Menukarte die noch in Auftrag gegeben werden.
Im Idealfall kann der Designer hierfür auch was mit designen das an einen Firma weitergeben werden kann um die 'Umschläge zu erstellen. Logo kann muss nicht mit drin sein. Es geht auch sehr um die einfache Darstellung des Ganzen.

```html
<!DOCTYPE html>
<html lang="de">
<head>
<meta charset="utf-8">
<title>Ristorante Miravalle – Menükarte</title>
<link rel="stylesheet" href="https://fonts.googleapis.com/css2?family=Roboto+Condensed:wght@700&family=Roboto:wght@400&display=swap">
<style>
  :root {
    --paper: #f1ebe1;
    --header: #231f20;
    --ink: #403f42;
    --price-box: #e0d9c4;
    --rule: #c5bba7;
    --sketch-a: #e6dfd3;
    --sketch-b: #d8d1c5;
  }
  * { margin: 0; padding: 0; box-sizing: border-box; }
  html, body { width: 735px; height: 1200px; overflow: hidden; }
  body { background: var(--paper); position: relative; font-family: "Roboto", Arial, sans-serif; color: var(--ink); }

  .masthead {
    position: absolute; left: 0; top: 0; width: 735px; height: 180px;
    background: var(--header);
    display: flex; align-items: center; justify-content: center;
  }
  .brand-name {
    font-family: "Roboto", Arial, sans-serif; font-weight: 400;
    color: var(--price-box); font-size: 26px; letter-spacing: 1px;
  }

  .rule { position: absolute; left: 85px; width: 580px; height: 1px; background: var(--rule); }

  .menu-title {
    position: absolute; left: 85px;
    font-family: "Roboto Condensed", "Arial Narrow", sans-serif; font-weight: 700;
    font-size: 49px; line-height: 1; letter-spacing: -1.5px; color: var(--ink);
  }
  .dish-list { position: absolute; left: 85px; list-style: none; font-size: 13px; line-height: 1.2; }
  .dish-list li { margin-bottom: 15.6px; }

  .price-tag {
    position: absolute; left: 527px; width: 108px; height: 108px;
    background: var(--price-box);
    display: flex; align-items: center; justify-content: center;
    font-family: "Roboto Condensed", "Arial Narrow", sans-serif; font-weight: 700;
    font-size: 46px; letter-spacing: -1px; color: var(--ink);
  }

  .vegetable-sketch {
    position: absolute; left: 23px; top: 956px; width: 672px; height: 204px;
    background: radial-gradient(ellipse at 50% 60%, var(--sketch-b) 0%, var(--sketch-a) 55%, rgba(241,235,225,0) 80%);
  }
  .footer-tab { position: absolute; left: 166px; top: 1170px; width: 403px; height: 30px; background: var(--price-box); }
</style>
</head>
<body>
  <header class="masthead">
    <div class="brand-name">Ristorante Miravalle</div>
  </header>

  <div class="rule" style="top:224px"></div>

  <section class="menu">
    <h2 class="menu-title" style="top:265px">MENU 1</h2>
    <ul class="dish-list" style="top:322px">
      <li>Appetithäppchen und Aperitif</li>
      <li>Italiensicher Aufschnitt Teller</li>
      <li>Pasta mit Hackfleischsoße und Sahne</li>
      <li>Kalbsbraten mit Barolosoße und Rosmarin Kartoffeln</li>
      <li>Zitronen Sorbet</li>
    </ul>
    <div class="price-tag" style="top:268px">49,-</div>
  </section>

  <div class="rule" style="top:480px"></div>

  <section class="menu">
    <h2 class="menu-title" style="top:520px">MENU 2</h2>
    <ul class="dish-list" style="top:577px">
      <li>Gemischter Salat</li>
      <li>Pasta mit scharfer Tomatensoße</li>
      <li>Putengeschnetzeltes in Currysoße mit Reis</li>
      <li>Tiramisu</li>
    </ul>
    <div class="price-tag" style="top:523px">35,-</div>
  </section>

  <div class="rule" style="top:700px"></div>

  <div class="vegetable-sketch" role="img" aria-label="Gezeichnete Gemüse-Illustration: Paprika, Zwiebeln, Knoblauch, Chilis, Karotten, Erbsen und Auberginen"></div>

  <section class="menu">
    <h2 class="menu-title" style="top:733px">MENU 3</h2>
    <ul class="dish-list" style="top:786px">
      <li>Aperitif</li>
      <li>Vitello Tonnato</li>
      <li>Lasagne im Ofen überbacken</li>
      <li>Rumpsteak tranchiert, auf Rucola Bett serviert mit<br>gehobelten Original Parmesan Käse</li>
      <li>Rosmarinkartoffeln und Gemüse</li>
      <li>Panna Cotta mit Waldfrüchte</li>
    </ul>
    <div class="price-tag" style="top:747px">55,-</div>
  </section>

  <div class="footer-tab"></div>
</body>
</html>
```